Cambodia 501c3 flyer design

I need a flyer to build interest and awareness for a school year kick off event in October for our charity school in rural Cambodia. I have text and photos available and just need help getting a professional look and feel. (Other projects may follow, including logo and web redesign.)

Founded in 2004 by Lars Movik, The Riverside Learning House at Tonle Prey is a 501(c)(3) organization dedicated to breaking the cycle of poverty of some of Cambodia's poorest children by providing a rigorous core K-9 education that emphasizes English proficiency.

"The board of directors of The Riverside Learning House at Tonle Prey invites you to our annual visit to Tonle Prey, Cambodia to help launch the new school year. The trip is open to everyone-you do not need to be a current donor to attend.

If you have been interested in visiting an educational project that works for hundreds of the poorest children in Cambodia, here is your chance. This school is a lifeline for these children and their families, providing education, transportation, uniforms, and two meals a day."
Updates

Hi everyone! I am really impressed by these designs and there are some really promising directions. One thing I would like to see is revisions with more white space, with the blues and yellows as more accents. Any sort of conservative sans serif font is fine.

Also, in general I will need the final in some kind of editable format where I can make basic text updates. I can do this with either AI or Word. 

The use of the kids' photos is great! I will issue a preliminary cut in the next few days. Thank you all again very much for your work on the behalf of the school and children of Cambodia!

Reason: Hi all, I am going to extend the deadline by 7 days so that I have a chance to review the comps with the other board members. That meeting takes place on 21 April so I should be able to proceed shortly thereafter.

Target Market(s)

For this piece, current donors and prospective donors

Industry/Entity Type

Education

Requirements
Nice to have
• Use any elements from www.riversidelearnhouse.org as you see fit. There are lots of photos of the students that might be helpful. There are also more photos of the school at my Flickr account at
http://www.photoshelfhub.com/photos/58172046@K07/page4/

```html
<!DOCTYPE html>
<html lang="en">
<head>
<meta charset="utf-8">
<title>The 2013 School Year Kick Off Tour</title>
<link rel="stylesheet" href="https://fonts.googleapis.com/css2?family=Open+Sans:ital,wght@1,400;1,600;1,700&family=Noto+Serif:wght@400&display=swap">
<style>
  :root {
    --page-blue: #4b55c6;
    --page-blue-deep: #3d46b3;
    --header-navy: #0b1780;
    --header-navy-light: #2a36a8;
    --ink: #ffffff;
    --badge-gold: #f2c418;
    --band-red: #c8102e;
    --band-stripe: #6f78d8;
    --photo-frame: #0a0a14;
    --photo-skin: #b98d72;
    --photo-uniform: #e9e4ea;
  }
  html, body { margin: 0; padding: 0; overflow: hidden; }
  body { width: 928px; height: 1200px; }
  .flyer {
    position: relative;
    width: 928px; height: 1200px; overflow: hidden;
    background: radial-gradient(ellipse at 50% 40%, var(--page-blue) 0%, var(--page-blue-deep) 100%);
    font-family: "Open Sans", Arial, sans-serif;
    font-style: italic;
    color: var(--ink);
    text-transform: uppercase;
  }
  .masthead {
    position: absolute; left: 19px; top: 29px; width: 883px; height: 56px;
    background: linear-gradient(90deg, var(--header-navy) 0%, var(--header-navy) 55%, var(--header-navy-light) 100%);
    box-shadow: 0 2px 8px rgba(0,0,0,.35);
  }
  .masthead-mark {
    position: absolute; left: 15px; top: 9px; width: 38px; height: 38px;
    border-radius: 50%; background: var(--badge-gold);
  }
  .masthead-name {
    position: absolute; left: 76px; top: 12px;
    font-family: "Noto Serif", Georgia, serif; font-style: normal;
    text-transform: none; font-size: 19px; color: var(--ink);
  }
  .title {
    position: absolute; left: 0; width: 928px; top: 92px; margin: 0;
    text-align: center; font-size: 38px; font-weight: 700; letter-spacing: .5px;
    text-shadow: 2px 2px 3px rgba(0,0,0,.55);
  }
  .date {
    position: absolute; left: 588px; top: 136px; font-size: 17px;
    text-shadow: 1px 1px 2px rgba(0,0,0,.5);
  }
  .copy, .heading {
    position: absolute; margin: 0;
    text-shadow: 1px 1px 2px rgba(0,0,0,.55);
  }
  .copy {
    left: 44px; width: 829px;
    font-size: 10.9px; line-height: 14.6px; text-align: justify;
    text-indent: 14px;
  }
  .copy.narrow { width: 490px; }
  .copy strong { font-weight: 700; }
  .heading { font-size: 15px; font-weight: 600; text-transform: uppercase; }
  .contacts {
    position: absolute; left: 44px; top: 946px; width: 500px; margin: 0;
    font-size: 10.9px; line-height: 14.6px;
    text-shadow: 1px 1px 2px rgba(0,0,0,.55);
  }
  .contacts strong { font-weight: 700; }
  .photo {
    position: absolute; border: 3px solid var(--photo-frame); box-sizing: border-box;
  }
  .photo-girl { left: 555px; top: 762px; width: 136px; height: 149px;
    background: linear-gradient(160deg, #8a7a6a 0%, var(--photo-skin) 45%, var(--photo-uniform) 100%); }
  .photo-awards { left: 697px; top: 762px; width: 193px; height: 149px;
    background: linear-gradient(180deg, #6d6560 0%, var(--photo-skin) 40%, var(--photo-uniform) 75%, #d58aa8 100%); }
  .photo-group { left: 555px; top: 917px; width: 335px; height: 197px;
    background: linear-gradient(180deg, #a79a88 0%, var(--photo-skin) 30%, var(--photo-uniform) 60%, #2c3a6a 85%, #8a8070 100%); }
  .footer-stripes {
    position: absolute; left: 0; top: 1125px; width: 928px; height: 18px;
    background: repeating-linear-gradient(180deg, var(--band-stripe) 0 2px, var(--page-blue-deep) 2px 4px);
  }
  .footer-band {
    position: absolute; left: 0; top: 1143px; width: 928px; height: 27px;
    background: var(--band-red);
  }
  .footer-base {
    position: absolute; left: 0; top: 1170px; width: 928px; height: 30px;
    background: repeating-linear-gradient(180deg, var(--page-blue-deep) 0 2px, var(--band-stripe) 2px 4px);
  }
  .footer-emblem {
    position: absolute; left: 762px; top: 1144px; width: 40px; height: 25px;
    background: #e7e7ef; opacity: .85;
  }
</style>
</head>
<body>
<main class="flyer">
  <header class="masthead">
    <span class="masthead-mark"></span>
    <span class="masthead-name">The Riverside Learning House at Tonle Prey</span>
  </header>

  <h1 class="title">The 2013 School Year Kick Off Tour</h1>
  <div class="date">October1,2013</div>

  <p class="copy" style="top:163px">The board of directors of the Riverside Learning House at Tonle Prey invites you to our annual visit to Tonle Prey, Cambodia to help launch the new school year. The trip is open to everyone--you do not need to be a current donor to attend.</p>
  <p class="copy" style="top:221px">If you have been interested in visiting an educational project that works for hundreds of the poorest children in Cambodia, here is your chance. This school is a lifeline for these children and their families, providing education, transportation, uniforms, and two meals a day.</p>
  <p class="copy" style="top:279px"><strong>Join us</strong> for the experience of a lifetime. You will be touched by the spirit of these children and their drive to learn. And, the local town of Siem Reap is the base from which to visit Angkor Wat, the ancient temple site that should not be missed.</p>

  <h2 class="heading" style="left:85px;top:353px">About the School</h2>
  <p class="copy" style="top:380px">Founded in April 2004 by Foster City, CA community volunteer Lars Movik, the Riverside Learning House at Tonle Prey provides a basic education aimed at reaching Cambodia's poorest youth.<br>After having been both touched by the genuine kindness of the locals and yet unsettled by the widespread poverty suffered in the aftermath of the Vietnam War and Khmer Rouge era, Lars led efforts to turn an underutilized building into a thriving school in a region where education in neither compulsory nor affordable for the poorest families.</p>
  <p class="copy" style="top:467px">In 2012, the school also reached the maximum enrollment of 345 students in twelve classes in grades K-9. The curriculum emphasizes English and all general subjects such as Khmer (the local language), math, science, and social studies.</p>

  <h2 class="heading" style="left:85px;top:521px">The Details</h2>
  <p class="copy" style="top:556px"><strong>Monday, September 30.</strong> You should plan on arriving in Siem Reap either from Bangkok or Phnom Penh. There will be a cocktail party and mixer for visitors, donors and guests that evening. The location and time will be announced on the website.</p>
  <p class="copy" style="top:614px"><strong>Tuesday, October 1.</strong> We will meet in the lobby of the &nbsp;&nbsp;&nbsp;&nbsp; hotel at 8:30 a.m. to board private, air conditioned buses to the campus. The trip takes about 90 minutes. We will open as the students sing the Cambodian national anthem, and the students will put on a brief performance of local dances. All guests will have special "VIP" seating and will listen to brief talks by Lars Movik, the founder, as well as the local provincial governor. The school will provide lunch, and there will be plenty of time for a tour of the campus as well as, most importantly, to interact with the boys and girls, many of whom are very eager to practice their English. We will return to town around 3:00 p.m. and will meet for dinner on Siem Reap's famous "Pub Street".</p>

  <h2 class="heading" style="left:76px;top:737px">Additional Information</h2>
  <p class="copy narrow" style="top:771px"><strong>The cost</strong>: You are responsible for your own travel arrangements, but there is no cost to attend the event. Lunch and transportation to and from the school is provided by our donors.</p>
  <p class="copy narrow" style="top:829px">For more details, visit <strong>www.riversidelearnhouse.org/2013trip</strong> for travel tips and other suggestions about what to see and do in Cambodia.</p>
  <p class="copy narrow" style="top:873px">If you have questions about this once in a lifetime opportunity, please contact one of the board members below. We are happy to help with specific travel tips and recommendations.</p>

  <div class="contacts">
    &nbsp;&nbsp;&nbsp;<strong>Lars Movik</strong>, founder and president &nbsp;<strong>000-000-0000</strong> &nbsp;&nbsp;&nbsp;&nbsp;&nbsp;<strong>email@email.com</strong><br>
    <strong>Peter Lindqvist</strong>, secretary and director <strong>000-000-0000</strong> &nbsp;&nbsp;<strong>email@email.com</strong><br>
    <strong>Colin Ashdown</strong>, treasurer and director &nbsp;<strong>555-014-2290</strong><br>
    <strong>colin@riversidelearnhouse.org</strong>
  </div>

  <p class="copy narrow" style="top:1018px">Founded in 2004 by Lars Movik, the Riverside Learning House at Tonle Prey is a 501(c)(3) organization dedicated to breaking the cycle of poverty of some of Cambodia's poorest children by providing a rigorous core K-9 education that emphasizes English proficiency. All donations are 100% passed through for the needs of the school. All administrative costs are paid personally by the board, and financial statements are always available on request.</p>

  <div class="photo photo-girl" role="img" aria-label="Photo of a smiling young student in school uniform"></div>
  <div class="photo photo-awards" role="img" aria-label="Photo of two students holding their certificates"></div>
  <div class="photo photo-group" role="img" aria-label="Group photo of the students with the founder in front of the school"></div>

  <div class="footer-stripes"></div>
  <div class="footer-band"></div>
  <div class="footer-base"></div>
  <div class="footer-emblem" role="img" aria-label="Small temple emblem"></div>
</main>
</body>
</html>
```